Tending Our Garden eBook Cover Design

I want to deisgn a cover for my eBook (FRONT COVER) and the title is:

Under the Willow Tree; Where I Found My Quiet Strength and Where You Might Too
By KT Dorran

TITLE CHANGED TO: UNDER THE WILLOW TREE; WHERE I FOUND MY QUIET STRENGTH AND WHERE YOU MIGHT TOO

The color palette is attached. Along with some photos options of me. Along with the ebook in WORD Document. My website is www.KTDorranLive.example. You can use a different color palette if you think it is best

Target Market(s)

women who look to build a personal brand

Industry/Entity Type

health and wellness

Requirements
Must have
• the title
Nice to have
• use my picture on the cover; but that is optional
Should not have
• any men

```html
<!DOCTYPE html>
<html lang="en">
<head>
<meta charset="utf-8">
<title>Under the Willow Tree — KT Dorran</title>
<link href="https://fonts.googleapis.com/css2?family=Cinzel:wght@400;700&family=Cinzel+Decorative:wght@700;900&display=swap" rel="stylesheet">
<style>
  :root {
    --page: #ffffff;
    --cover-black: #050407;
    --sky-pink: #d65aa0;
    --sky-light: #ec8ec3;
    --sky-deep: #a2407f;
    --ridge: #5e2448;
    --title-pink: #ee8ca3;
    --title-white: #ffffff;
  }
  * { margin: 0; padding: 0; box-sizing: border-box; }
  html, body {
    width: 848px;
    height: 1200px;
    overflow: hidden;
    background: var(--page);
  }
  .canvas {
    position: relative;
    width: 848px;
    height: 1200px;
    background: var(--page);
  }
  .cover {
    position: absolute;
    left: 94px;
    top: 205px;
    width: 659px;
    height: 789px;
    background: var(--cover-black);
    overflow: hidden;
  }
  .cover-photo {
    position: absolute;
    left: 0;
    top: 0;
    width: 659px;
    height: 460px;
    background:
      radial-gradient(circle at 51% 18%, #ffffff 0, #fbd9ec 4%, rgba(236,142,195,0.9) 14%, rgba(214,90,160,0) 45%),
      linear-gradient(180deg, var(--sky-deep) 0%, var(--sky-pink) 35%, var(--sky-light) 58%, var(--sky-pink) 68%, var(--ridge) 82%, var(--cover-black) 100%);
  }
  .title-block {
    position: absolute;
    left: 0;
    top: 470px;
    width: 659px;
    text-align: center;
  }
  .title-main,
  .title-sub {
    font-family: "Cinzel Decorative", "Cinzel", serif;
    font-weight: 900;
    line-height: 1;
    white-space: nowrap;
  }
  .title-main {
    font-size: 46px;
    color: var(--title-pink);
    letter-spacing: 0.5px;
  }
  .title-sub {
    margin-top: 12px;
    font-size: 27px;
    color: var(--title-white);
  }
  .title-main + .title-sub { margin-top: 20px; }
  .title-sub.accent {
    margin-top: 14px;
    color: var(--title-pink);
  }
  .author {
    margin-top: 24px;
    font-family: "Cinzel", serif;
    font-weight: 400;
    font-size: 33px;
    line-height: 1;
    color: var(--title-white);
    letter-spacing: 1px;
  }
</style>
</head>
<body>
  <main class="canvas">
    <section class="cover">
      <div class="cover-photo" role="img" aria-label="Silhouette of a woman with raised arms on a mountain peak at a pink sunset, bright sunburst behind her and banknotes floating in the air"></div>
      <div class="title-block">
        <h1 class="title-main">Under the Willow</h1>
        <p class="title-sub">Tree; Where I Found</p>
        <p class="title-sub">My Quiet Strength</p>
        <p class="title-sub accent">And Where You Might Too</p>
        <p class="author">KT Dorran</p>
      </div>
    </section>
  </main>
</body>
</html>
```